Accountability Project Graphics

I want to create 10 social media graphics (new Instagram size 4:5 (1080 x 1350 pixels) focusing on our Kelmora Accountability App, using any of the 3 pictures attached. Use the attached pics only, NO RANDOM STOCK PHOTOGRAPHY. For the color scheme, use the landing page colors/fonts (attached).
You can add any of the 3 photos attached but I mainly need BOLD text that includes these headlines and sub-headlines on them.
Please NOTE for all the headlines below, also add this sub-headline on each graphic:
Stay Consistent with MB in Your Pocket!
Here are the headlines:
• Stop Starting Over Every Monday
• You don't need more willpower. You need more support
• Built for women who are tired of doing this alone
• When Motivation Fades, MB Checks In
• The Support System You've Been Missing
• Support When Motivation Disappears
• What if MB Checked in Every Day?
• The Missing Piece Isn't Another Diet
• Eat the food you love. Stay accountable every day.
• One Bad Meal Doesn't Mean You Failed
women over 40 trying to lose weight

```html
<!DOCTYPE html>
<html lang="en">
<head>
<meta charset="UTF-8">
<title>Accountability Project Graphics</title>
<link href="https://fonts.googleapis.com/css2?family=Bebas+Neue&family=Kaushan+Script&family=Poppins:wght@400;500&display=swap" rel="stylesheet">
<style>
  :root {
    --canvas-bg: #ececee;
    --ink: #111111;
    --hot-pink: #ec1763;
    --blush: #f6a9c6;
    --blush-light: #fde6ee;
    --white: #ffffff;
    --plum-deep: #6e0b4c;
    --plum: #b0137a;
    --willpower-pink: #f58cc3;
    --photo-dark: #1d1b26;
    --photo-skin: #8a5a45;
  }
  * { margin: 0; padding: 0; box-sizing: border-box; }
  html, body { width: 768px; height: 1200px; overflow: hidden; }
  body { background: var(--canvas-bg); position: relative; font-family: "Poppins", sans-serif; }

  .post { position: absolute; overflow: hidden; box-shadow: 0 6px 18px rgba(0,0,0,0.18); }
  .band { position: absolute; left: 0; right: 0; bottom: 0; background: var(--hot-pink); }
  .photo { position: absolute; }

  /* Main post: Stop Starting Over */
  .post-monday {
    left: 124px; top: 36px; width: 520px; height: 650px;
    background: linear-gradient(180deg, var(--white) 0%, var(--blush-light) 30%, var(--blush) 75%, #f28bb2 100%);
  }
  .post-monday .band { height: 32px; }
  .post-monday .photo {
    left: 318px; top: 150px; width: 202px; height: 468px;
    border-radius: 101px 101px 0 0;
    background: linear-gradient(180deg, var(--photo-skin) 0%, var(--photo-dark) 24%, var(--photo-dark) 100%);
  }
  .monday-copy { position: absolute; left: 43px; top: 62px; width: 266px; z-index: 1; }
  .script-word {
    font-family: "Kaushan Script", cursive; color: var(--hot-pink);
    font-size: 100px; line-height: 1; transform: rotate(-6deg); display: block; text-align: center;
  }
  .monday-headline {
    font-family: "Bebas Neue", sans-serif; color: var(--ink);
    font-size: 56px; line-height: 0.94; margin-top: 2px; text-align: left; white-space: nowrap;
  }
  .monday-sub {
    color: var(--hot-pink); font-size: 20px; line-height: 1.18; margin-top: 8px; text-align: center;
  }

  /* Built for women post */
  .post-women {
    left: 32px; top: 736px; width: 336px; height: 420px;
    background: var(--white);
  }
  .post-women .band { height: 18px; }
  .post-women .photo {
    left: 0; top: 140px; width: 336px; height: 262px;
    background: linear-gradient(135deg, #6d5a6a 0%, #c96b8e 45%, #f3b9cf 80%, #fbe0ea 100%);
  }
  .women-headline {
    position: absolute; left: 16px; top: 26px;
    font-family: "Bebas Neue", sans-serif; color: var(--ink); font-size: 50px; line-height: 0.9;
  }
  .women-headline .accent { color: var(--hot-pink); }
  .women-kicker {
    position: absolute; left: 16px; top: 72px;
    font-family: "Bebas Neue", sans-serif; color: var(--ink); font-size: 23px; line-height: 1;
  }
  .women-sub {
    position: absolute; right: 16px; top: 102px; width: 130px;
    color: var(--hot-pink); font-size: 10px; line-height: 1.2; text-align: right;
  }

  /* Willpower post */
  .post-support {
    left: 400px; top: 736px; width: 336px; height: 420px;
    background: linear-gradient(160deg, var(--plum-deep) 0%, var(--plum) 55%, #8c0d62 100%);
  }
  .post-support .photo {
    left: 124px; top: 168px; width: 212px; height: 252px;
    border-radius: 90px 90px 0 0;
    background: linear-gradient(180deg, #3b2a3a 0%, #3c4f78 40%, #5876a8 100%);
  }
  .support-copy { position: absolute; left: 0; right: 0; top: 14px; text-align: center; }
  .support-copy .script-word { color: var(--white); font-size: 78px; }
  .support-headline {
    font-family: "Bebas Neue", sans-serif; color: var(--willpower-pink);
    font-size: 33px; line-height: 0.98; margin-top: 4px;
  }
  .support-sub {
    position: absolute; left: 16px; top: 236px; width: 100px;
    color: var(--white); font-size: 15px; line-height: 1.2;
  }
</style>
</head>
<body>
  <section class="post post-monday">
    <div class="photo" role="img" aria-label="Photo of MB smiling in a black mesh top and black jeans, hand on hip"></div>
    <div class="monday-copy">
      <span class="script-word">Stop</span>
      <h1 class="monday-headline">Starting Over<br>Every Monday</h1>
      <p class="monday-sub">Stay Consistent with<br>MB in Your Pocket!</p>
    </div>
    <div class="band"></div>
  </section>

  <section class="post post-women">
    <h2 class="women-headline">Built for <span class="accent">Women</span></h2>
    <p class="women-kicker">Who are tired of doing this alone</p>
    <p class="women-sub">Stay Consistent with<br>MB in Your Pocket!</p>
    <div class="photo" role="img" aria-label="Photo of two women hugging and laughing in a store"></div>
    <div class="band"></div>
  </section>

  <section class="post post-support">
    <div class="support-copy">
      <span class="script-word">You</span>
      <h2 class="support-headline">Don't need more willpower.<br>You need more support</h2>
    </div>
    <p class="support-sub">Stay Consistent with MB in Your Pocket!</p>
    <div class="photo" role="img" aria-label="Photo of two women in denim jackets laughing together"></div>
  </section>
</body>
</html>
```